Small Business Broker Business Card Design

A business card design for a small business brokerage, which is a financial service, not unlike real estate brokerage, but for small businesses such as laundromats, pizza shops, restaurants, cleaners etc. The designs should all be simple, more conservative in nature, using the colors and font of the logo. Again, think real estate Brokerage as a business context
Contact Information for Business Card
Name: Dale R. Whitmore. Title: Small Business Advisor. Email: d.whitmore@lanternbridgeadvisory.com. Mobile: (917) 555-0148. Office: (718) 555-0193. www.lanternbridgeadvisory.com

```html
<!DOCTYPE html>
<html lang="en">
<head>
<meta charset="utf-8">
<title>Lanternbridge Advisory – Business Card</title>
<link rel="stylesheet" href="https://fonts.googleapis.com/css2?family=Montserrat:wght@600;700&family=Open+Sans:wght@400;700&display=swap">
<style>
  :root {
    --stage: #585858;
    --navy: #1b3a6b;
    --navy-deep: #163260;
    --navy-soft: #23457a;
    --green: #8dc63f;
    --white: #ffffff;
    --line-tint: #dfe5ee;
  }
  * { box-sizing: border-box; margin: 0; padding: 0; }
  html, body { width: 1200px; height: 1200px; overflow: hidden; }
  body { background: var(--stage); position: relative; }

  .card {
    position: absolute;
    left: 226px;
    width: 746px;
    height: 436px;
    border-radius: 35px;
    overflow: hidden;
  }
  .card--front { top: 140px; background: var(--navy); }
  .card--back { top: 627px; background: var(--white); }

  .front-texture {
    position: absolute; inset: 0;
    background: linear-gradient(120deg, var(--navy-deep) 0%, var(--navy) 50%, var(--navy-soft) 100%);
  }

  .brand {
    position: absolute;
    left: 71px; top: 230px;
    display: flex; align-items: center; gap: 22px;
  }
  .brand__square { width: 70px; height: 70px; background: var(--white); }
  .brand__name {
    font-family: "Montserrat", sans-serif;
    font-weight: 700;
    font-size: 25px;
    letter-spacing: 0.5px;
    color: var(--white);
    text-transform: uppercase;
    line-height: 1;
  }
  .brand__tagline {
    margin-top: 9px;
    font-family: "Montserrat", sans-serif;
    font-weight: 600;
    font-size: 13.4px;
    letter-spacing: 1.6px;
    color: var(--green);
    text-transform: uppercase;
  }

  .back-art { position: absolute; left: 300px; top: 30px; width: 446px; height: 380px; }

  .contact {
    position: absolute;
    left: 0; width: 426px; top: 124px;
    text-align: center;
    color: var(--navy);
  }
  .contact__name {
    font-family: "Montserrat", sans-serif;
    font-weight: 700;
    font-size: 22px;
    letter-spacing: 0.5px;
    text-transform: uppercase;
  }
  .contact__title {
    margin-top: 4px;
    font-family: "Montserrat", sans-serif;
    font-weight: 600;
    font-size: 11px;
    letter-spacing: 0.8px;
    color: var(--green);
    text-transform: uppercase;
  }
  .contact__icons { margin-top: 22px; display: flex; justify-content: center; gap: 5px; }
  .contact__phones {
    margin-top: 10px;
    font-family: "Open Sans", sans-serif;
    font-weight: 700;
    font-size: 17px;
    line-height: 25px;
  }
  .contact__web {
    margin-top: 25px;
    font-family: "Open Sans", sans-serif;
    font-weight: 400;
    font-size: 17px;
    line-height: 22px;
  }
</style>
</head>
<body>

<section class="card card--front" aria-label="Card front">
  <div class="front-texture" role="img" aria-label="Subtle repeating tonal pattern in navy blue"></div>
  <div class="brand">
    <div class="brand__square"></div>
    <div class="brand__text">
      <div class="brand__name">Lanternbridge Advisory, Inc</div>
      <div class="brand__tagline">Confidently buy or sell a local business today</div>
    </div>
  </div>
</section>

<section class="card card--back" aria-label="Card back">
  <svg class="back-art" viewBox="0 0 446 380" role="img" aria-label="Faint decorative line graphic in grey-blue and light green">
    <defs>
      <linearGradient id="artFade" x1="0" y1="1" x2="1" y2="0">
        <stop offset="0" stop-color="#ffffff" stop-opacity="0"/>
        <stop offset="1" stop-color="#dfe5ee" stop-opacity="0.9"/>
      </linearGradient>
    </defs>
    <rect width="446" height="380" fill="url(#artFade)"/>
  </svg>

  <div class="contact">
    <div class="contact__name">Dale R. Whitmore</div>
    <div class="contact__title">Small Business Advisor</div>
    <div class="contact__icons">
      <svg width="32" height="32" viewBox="0 0 32 32" aria-label="Mobile">
        <circle cx="16" cy="16" r="16" fill="#8dc63f"/>
        <rect x="11" y="7" width="10" height="18" rx="2" fill="none" stroke="#fff" stroke-width="2"/>
        <line x1="14.5" y1="22" x2="17.5" y2="22" stroke="#fff" stroke-width="1.5"/>
      </svg>
      <svg width="32" height="32" viewBox="0 0 32 32" aria-label="Office phone">
        <circle cx="16" cy="16" r="16" fill="#8dc63f"/>
        <path d="M11 8c1-.6 2-.3 2.5.6l1.4 2.6c.4.8.2 1.6-.5 2.1l-1 .7c.8 2 2.4 3.7 4.5 4.6l.8-1c.5-.7 1.4-.9 2.1-.5l2.6 1.4c.9.5 1.2 1.6.6 2.5l-.9 1.4c-.6.9-1.7 1.3-2.8 1-5.2-1.5-9.2-5.5-10.7-10.7-.3-1.1.1-2.2 1-2.8z" fill="#fff"/>
      </svg>
    </div>
    <div class="contact__phones">
      <div>(917) 555-0148</div>
      <div>(718) 555-0193</div>
    </div>
    <div class="contact__web">
      <div>d.whitmore@lanternbridgeadvisory.com</div>
      <div>lanternbridgeadvisory.com</div>
    </div>
  </div>
</section>

</body>
</html>
```